Flyer für dynamisches Maklerteam
The design process with Brightwing went very well. He responded precisely to our requirements and to our target group and developed designs that reflect our logo and our corporate identity in many small details. Communication with Brightwing went great. He quickly translated our requests into wonderful designs and created flyers that we are very happy with. Brightwing is a good designer and I can highly recommend working with him. Dr. Ilse Brandvoort KORVEN Real Estate
Zielgruppe
KORVEN Immobilien ist ein dynamisches Maklerteam, dass sich auf den Verkauf von Wohnimmobilien des gehobenen Preissegmentes spezialisiert hat. Unser Schwerpunkt liegt auf Luxusobjekten.
Hallo,
schön, dass ihr an unserem Design-Wettbewerb teilnehmt.
Unser Zielgruppe sind verkaufswillige Eigentümer hochpreisiger Immobilien.
--> eine ganz wichtige Kundengruppe sind Erben, die ihre geerbte Immobilie verkaufen wollen.
Wir wünschen uns beidseitig bedruckte Flyer auf hochwertigem Material (Chromosulfatpapier, 450 g/m²). Bei der Auswahl des Formates wollen wir euch freie Hand lassen.
Vorderseite:
- Logo von KORVEN Immobilien.
- Ein Foto als Eye-Catcher, das Interesse weckt, zum Schmunzeln bringt und in Erinnerung bleibt. Wichtig: Auf dem Foto sollte man Freude sehen (gerne lächelnde Gesichter, die Personen müssen nicht zwangsläufig in die Kamera blicken. Eine positive und glückliche Grundstimmung auf dem Bild ist wichtig). -> an dieser Stelle bitte geeignete Stock-Bilder recherchieren und diese vorschlagen.
- Claim: Genießen Sie Ihre Freiheit. Wir verkaufen Ihre Immobilie.
Rückseite:
folgenden Text bitte verwenden:
Das Besondere bei KORVEN Immobilien:
- langjährige Erfahrung mit Immobilien des gehobenen Segments
- hochprofessionelle Komplettabwicklung in kürzester Zeit
- ausgezeichnete Referenzen
- auf Wunsch sehr diskrete Abwicklung
Anschließend bitte einen Satz, der eine Abschlussfrage formuliert, die etwa folgenden Inhalt wiedergibt:
'Wenn Sie direkt mit uns sprechen möchten, erreichen Sie uns jederzeit unter 0157 - 3948 2036.'
(Diesen Satz könnt ihr gerne umformulieren.)
Website und Emailadresse [ www.korven-immobilien.example - ib@korven-immobilien.example ]
Bilder des gesamten KORVEN Verkaufsteam als Einzelportraits vor dunklem Hintergrund.
Dabei wichtig: Lorenz Korven als Chef bitte an die erste Stelle setzen. Henrike und Jonas Weidlich sind ein Ehepaar, die Immobilien meist gemeinsam verkaufen, daher bitte auch ihre beiden Portraits nebeneinander platzieren.
Bei der Gestaltung des Flyers i..

```html
<!DOCTYPE html>
<html lang="de">
<head>
<meta charset="utf-8">
<title>KORVEN Immobilien – Flyer</title>
<link href="https://fonts.googleapis.com/css2?family=Cinzel:wght@400;500&family=Jost:wght@300;400&display=swap" rel="stylesheet">
<style>
  :root {
    --navy: #252b5a;
    --paper: #ffffff;
    --ink: #ffffff;
    --soft-ink: #e6e8f2;
    --portrait-dark: #1b1b1f;
    --portrait-mid: #3a3432;
  }
  * { margin: 0; padding: 0; box-sizing: border-box; }
  html, body { width: 1200px; height: 849px; overflow: hidden; background: var(--paper); }
  .sheet { position: relative; width: 1200px; height: 849px; }
  .panel {
    position: absolute; top: 122px; width: 272px; height: 583px;
    background: var(--navy); color: var(--ink); overflow: hidden;
  }
  .panel--front-a { left: 30px; }
  .panel--back-a  { left: 313px; }
  .panel--front-b { left: 616px; }
  .panel--back-b  { left: 899px; }

  .brand {
    position: absolute; left: 0; right: 0; text-align: center;
    font-family: "Cinzel", serif; font-weight: 400; color: var(--ink);
    display: flex; justify-content: center; align-items: center; gap: 8px;
    letter-spacing: 0.08em;
  }
  .brand__dot { display: inline-block; background: var(--ink); border-radius: 50%; }
  .brand--large { top: 78px; font-size: 30px; }
  .brand--large .brand__dot { width: 9px; height: 9px; }
  .brand--hero { top: 88px; font-size: 34px; }
  .brand--hero .brand__dot { width: 10px; height: 10px; }
  .brand--small { top: 34px; font-size: 17px; }
  .brand--small .brand__dot { width: 6px; height: 6px; }

  .photo { position: absolute; left: 33px; width: 207px; }
  .photo--couple {
    top: 194px; height: 265px;
    background: linear-gradient(180deg, #c89a62 0%, #e39a4a 35%, #7a4a2c 70%, #3b2a22 100%);
  }
  .photo--jump {
    top: 188px; height: 319px;
    background: linear-gradient(180deg, #2c4aa3 0%, #3a63c4 60%, #5c89dd 100%);
  }
  .photo__caption {
    position: absolute; left: 62px; top: 62px;
    font-family: "Cinzel", serif; font-size: 8px; letter-spacing: 0.05em;
    color: var(--ink); transform: rotate(15deg); transform-origin: left top;
    white-space: nowrap;
  }

  .claim {
    position: absolute; left: 0; right: 0; text-align: center;
    font-family: "Cinzel", serif; font-weight: 400; font-size: 13px; line-height: 21px;
    letter-spacing: 0.04em; color: var(--soft-ink);
  }
  .claim--front-a { top: 476px; }
  .claim--front-b { top: 531px; }

  .usp-title {
    position: absolute; left: 0; right: 0; top: 100px; text-align: center;
    font-family: "Cinzel", serif; font-weight: 400; font-size: 10.5px; letter-spacing: 0.02em;
    white-space: nowrap;
  }
  .usp-list {
    position: absolute; left: 28px; top: 128px; width: 192px; list-style: none;
    font-family: "Jost", sans-serif; font-weight: 300; font-size: 10.5px; line-height: 14px;
  }
  .usp-list li { padding-left: 6px; text-indent: -6px; margin-bottom: 5px; }
  .usp-list li::before { content: "- "; }

  .team {
    position: absolute; left: 4px; top: 249px; width: 264px;
    display: grid; grid-template-columns: repeat(3, 86px); gap: 3px;
  }
  .team__portrait {
    height: 86px;
    background: radial-gradient(circle at 50% 45%, var(--portrait-mid) 0%, var(--portrait-dark) 70%);
  }

  .contact { position: absolute; left: 0; right: 0; text-align: center; }
  .contact__intro {
    top: 460px; font-family: "Jost", sans-serif; font-weight: 300; font-size: 10.5px;
  }
  .contact__phone {
    top: 478px; display: flex; justify-content: center; align-items: center; gap: 10px;
    font-family: "Cinzel", serif; font-size: 14px; letter-spacing: 0.04em;
  }
  .contact__web {
    top: 526px; font-family: "Cinzel", serif; font-size: 11.5px; letter-spacing: 0.03em;
  }
  .contact__mail {
    top: 545px; font-family: "Jost", sans-serif; font-weight: 300; font-size: 10px;
  }

  .page-number {
    position: absolute; top: 778px; font-family: "Jost", sans-serif; font-size: 26px; color: #000;
  }
  .page-number--3 { left: 571px; }
  .page-number--4 { left: 1154px; }
</style>
</head>
<body>
<main class="sheet">

  <section class="panel panel--front-a">
    <div class="brand brand--large"><span class="brand__dot"></span>KORVEN</div>
    <div class="photo photo--couple" role="img" aria-label="Paar mit Hüten spaziert bei Sonnenuntergang am Seeufer"></div>
    <p class="claim claim--front-a">Genießen Sie Ihre Freiheit.<br>Wir verkaufen Ihre Immobilie.</p>
  </section>

  <section class="panel panel--back-a">
    <div class="brand brand--small"><span class="brand__dot"></span>KORVEN</div>
    <h2 class="usp-title">Das Besondere bei KORVEN Immobilien:</h2>
    <ul class="usp-list">
      <li>langjährige Erfahrung mit Immobilien des gehobenen Segments</li>
      <li>hochprofessionelle Komplettabwicklung in kürzester Zeit</li>
      <li>ausgezeichnete Referenzen</li>
      <li>auf Wunsch sehr diskrete Abwicklung</li>
    </ul>
    <div class="team">
      <div class="team__portrait" role="img" aria-label="Portrait Lorenz Korven"></div>
      <div class="team__portrait" role="img" aria-label="Portrait Teammitglied"></div>
      <div class="team__portrait" role="img" aria-label="Portrait Dr. Ilse Brandvoort"></div>
      <div class="team__portrait" role="img" aria-label="Portrait Henrike"></div>
      <div class="team__portrait" role="img" aria-label="Portrait Jonas Weidlich"></div>
      <div class="team__portrait" role="img" aria-label="Portrait Teammitglied"></div>
    </div>
    <p class="contact contact__intro">Wir helfen Ihnen gerne weiter.</p>
    <p class="contact contact__phone">
      <svg width="22" height="22" viewBox="0 0 22 22" aria-hidden="true"><circle cx="11" cy="11" r="11" fill="#fff"/><path d="M8 5.5c-.8.3-1.8 1.3-1.8 2.6 0 3 3.6 8.3 7.4 8.4 1.2 0 2-.7 2.3-1.5l-2.2-1.8-1.3 1c-1.3-.6-2.9-2.8-3.2-4.3l1.2-.9z" fill="#252b5a"/></svg>
      + 49 (0) 0157 - 3948 2036
    </p>
    <p class="contact contact__web">www.korven-immobilien.example</p>
    <p class="contact contact__mail">ib@korven-immobilien.example</p>
  </section>

  <section class="panel panel--front-b">
    <div class="brand brand--hero"><span class="brand__dot"></span>KORVEN</div>
    <div class="photo photo--jump" role="img" aria-label="Fröhlicher Golfer springt mit erhobenem Schläger vor blauem Himmel">
      <span class="photo__caption">Genießen Sie Ihre Freiheit.</span>
    </div>
    <p class="claim claim--front-b">Wir verkaufen Ihre Immobilie.</p>
  </section>

  <section class="panel panel--back-b">
    <div class="brand brand--small"><span class="brand__dot"></span>KORVEN</div>
    <h2 class="usp-title">Das Besondere bei KORVEN Immobilien:</h2>
    <ul class="usp-list">
      <li>langjährige Erfahrung mit Immobilien des gehobenen Segments</li>
      <li>hochprofessionelle Komplettabwicklung in kürzester Zeit</li>
      <li>ausgezeichnete Referenzen</li>
      <li>auf Wunsch sehr diskrete Abwicklung</li>
    </ul>
    <div class="team">
      <div class="team__portrait" role="img" aria-label="Portrait Lorenz Korven"></div>
      <div class="team__portrait" role="img" aria-label="Portrait Teammitglied"></div>
      <div class="team__portrait" role="img" aria-label="Portrait Dr. Ilse Brandvoort"></div>
      <div class="team__portrait" role="img" aria-label="Portrait Henrike"></div>
      <div class="team__portrait" role="img" aria-label="Portrait Jonas Weidlich"></div>
      <div class="team__portrait" role="img" aria-label="Portrait Teammitglied"></div>
    </div>
    <p class="contact contact__intro">Wir helfen Ihnen gerne weiter.</p>
    <p class="contact contact__phone">
      <svg width="22" height="22" viewBox="0 0 22 22" aria-hidden="true"><circle cx="11" cy="11" r="11" fill="#fff"/><path d="M8 5.5c-.8.3-1.8 1.3-1.8 2.6 0 3 3.6 8.3 7.4 8.4 1.2 0 2-.7 2.3-1.5l-2.2-1.8-1.3 1c-1.3-.6-2.9-2.8-3.2-4.3l1.2-.9z" fill="#252b5a"/></svg>
      + 49 (0) 0157 - 3948 2036
    </p>
    <p class="contact contact__web">www.korven-immobilien.example</p>
    <p class="contact contact__mail">ib@korven-immobilien.example</p>
  </section>

  <span class="page-number page-number--3">3</span>
  <span class="page-number page-number--4">4</span>
</main>
</body>
</html>
```